Webdesign for large cottage directory

We have developed a first version of a website that can accommodate large groups (10 to 300 people). The site is English and is aimed at a wide audience ranging from a group of students to a family or a family. For the visitors the site is free and it is the propietaires who pay to see their accommodation. The site is online with just a few fake lodgings and a simple design to the elements that must be appraised (nothing to keep the current design). Our website is here: 456abri.com (login / pass = admin / 123) Home page (456abri.com): on this page section) and lodging by theme (third section). These three points should be highlighted as possible. The displayed map may be slightly modified. Only the background and the color changes when hovering over the mouse. It can be enlarged / retreciated. Below these 3 sections we have some fairly published articles, the latest blog posts and the footer. The menu will be visible throughout the site. Category page (https://456abri.fr/gite-departement/aveyron OR https://456abri.fr/gites-couchages-121): On these pages we always return the same format with the googlemap, an image 1 text. Below the list of the cottages concerned and the filter options. Product page: The pages presenting the cottages can be of two types: - Either the cottage has no owner and there is no contact for the visitor to the owner that he can retrieve his cottage by registering: example of a page of this type: https://456abri.fr/domaine-de-varnoquet - The cottage to a propietaire and we are on the classic card. : // 456abri. en / domain-of-varnoquet2 For all products on the site we have nav tab. It's just for testing. We do not want to be in the design for real website. All information must be in the page without login / register page: classic, it's here: https://456abri.it/login and https://456abri.fr/register Blog homepage (https://456abri.fr/blog ): Classic blog page Blog post (https://456abri.fr/blog/urltemporaire1551521154) and static page (https://456abri.fr/blog/Systeme-classement-456abrifr): Nothing special Menu: Menu is an important part of the website. It's the way to navigate on the wbesite.
Number of Pages Required
4 page
Colors
Designer to choose colors to be used in the design.
Look and feel

```html
<!DOCTYPE html>
<html lang="en">
<head>
<meta charset="utf-8">
<title>Vastelodge – Large group holiday lodgings</title>
<link rel="stylesheet" href="https://fonts.googleapis.com/css2?family=Raleway:wght@400;500;600;700&family=Open+Sans:wght@400;600;700&display=swap">
<style>
:root{
  --brand:#c8115f;
  --ink:#2b2b2b;
  --muted:#777;
  --line:#e2e2e2;
  --soft:#f4f4f4;
  --footer:#1f1f1f;
  --footer-deep:#141414;
  --ad:#cfcfcf;
}
*{box-sizing:border-box;margin:0;padding:0}
html,body{width:1200px;height:4091px;overflow:hidden}
body{font-family:"Open Sans",Arial,sans-serif;color:var(--ink);background:#fff;font-size:13px;position:relative}
h1,h2,h3,h4{font-family:"Raleway",Arial,sans-serif}
.wrap{width:860px;margin:0 auto;position:relative}

.topbar{height:27px;border-bottom:1px solid var(--line);font-size:10px;color:var(--muted)}
.topbar .wrap{display:flex;justify-content:flex-end;gap:26px;align-items:center;height:27px}
.topbar span{display:flex;align-items:center;gap:5px;white-space:nowrap}

.nav{height:55px}
.nav .wrap{display:flex;align-items:center;justify-content:space-between;height:55px}
.logo{display:flex;align-items:center;gap:8px;font-family:"Raleway",sans-serif;font-weight:500;font-size:22px;color:var(--ink)}
.logo i{display:block;width:12px;height:12px;background:var(--brand)}
.menu{display:flex;gap:4px;font-family:"Raleway",sans-serif;font-weight:700;font-size:11px}
.menu a{color:var(--ink);text-decoration:none;padding:18px 12px;letter-spacing:.4px}
.menu a.active{color:var(--brand);border-bottom:3px solid var(--brand)}

.hero{height:498px;position:relative;background:linear-gradient(100deg,#3b3a2c 0%,#7a5b40 30%,#a56b4f 55%,#5f5a3c 80%,#2f3025 100%)}
.hero-title{position:absolute;top:160px;width:100%;text-align:center;color:#fff;font-family:"Raleway",sans-serif;font-weight:700;font-size:52px;letter-spacing:2px}
.arrow{position:absolute;top:170px;width:34px;height:34px;display:flex;align-items:center;justify-content:center}
.arrow.left{left:120px}.arrow.right{right:120px}
.search{position:absolute;left:170px;top:357px;width:860px;height:88px;background:#fff;display:flex;align-items:flex-end;padding:0 26px 22px;gap:20px}
.field{flex:0 0 200px}
.field label{display:block;font-size:9px;font-weight:600;letter-spacing:.5px;color:var(--muted);margin-bottom:7px}
.field .input{height:26px;border:1px solid #d6d6d6;font-size:9px;color:#999;padding:6px 8px}
.btn{display:inline-block;background:var(--brand);color:#fff;font-weight:700;font-size:10px;letter-spacing:.5px;text-align:center}
.search .btn{width:172px;height:26px;line-height:26px;margin-left:10px}

.welcome{height:426px;padding-top:62px}
.welcome .wrap{display:flex;justify-content:space-between}
.welcome-text{width:470px}
.welcome h2{font-size:38px;font-weight:500;color:var(--ink)}
.welcome .sub{display:inline-block;margin-top:6px;font-size:17px;color:#444;text-decoration:underline;text-underline-offset:4px}
.welcome p{margin-top:22px;font-size:12px;line-height:1.7;color:var(--muted)}
.welcome .btn{margin-top:24px;padding:9px 20px;font-size:10px}
.welcome-photo{width:205px;height:250px;margin-right:-30px;background:linear-gradient(170deg,#b7d0e6 0%,#d8a37b 35%,#c66a56 60%,#7b7a6e 100%);box-shadow:0 6px 18px rgba(0,0,0,.3)}

.capacity{height:324px;background:linear-gradient(180deg,#1d2a44 0%,#2d4a6a 40%,#3d6f83 65%,#6b5b45 100%);color:#fff;text-align:center;padding-top:62px}
.capacity h2{font-size:34px;font-weight:500}
.capacity .lead{font-size:13px;margin-top:6px;opacity:.9}
.cap-row{display:flex;justify-content:center;gap:18px;margin-top:28px}
.cap{width:112px}
.cap .num{height:46px;background:var(--brand);font-family:"Raleway",sans-serif;font-weight:600;font-size:22px;line-height:46px}
.cap small{display:block;font-size:9px;margin-top:8px;opacity:.9}

.department{height:630px;padding-top:40px}
.section-title{text-align:center;font-size:34px;font-weight:500;color:#333}
.dept-body{display:flex;margin-top:55px;gap:55px}
.dept-map{width:440px;height:440px;margin-left:-5px;background:#fff;box-shadow:0 4px 16px rgba(0,0,0,.25);padding:18px}
.dept-map .fill{width:100%;height:100%;background:linear-gradient(160deg,#ecebe8,#dcdad6)}
.dept-info{width:330px;padding-top:68px}
.dept-info h3{color:var(--brand);font-size:22px;font-weight:700}
.dept-info .kind{font-size:13px;margin-top:4px}
.dept-info p{font-size:11px;line-height:1.7;color:#666;margin-top:14px}
.maps-label{display:flex;align-items:center;gap:10px;margin-top:12px;font-size:22px;color:#555}

.themes{height:870px;background:var(--soft);padding-top:68px}
.themes .lead{text-align:center;font-size:13px;color:var(--muted);margin-top:6px}
.theme-grid{display:grid;grid-template-columns:repeat(4,205px);gap:12px;margin:60px 0 0 10px}
.tile{height:205px;display:flex;align-items:center;justify-content:center;text-align:center;color:#fff;font-family:"Raleway",sans-serif;font-weight:700;font-size:17px;padding:0 24px;text-shadow:0 1px 3px rgba(0,0,0,.6)}
.t1{background:linear-gradient(160deg,#4a3a2c,#8a6b4f)}
.t2{background:linear-gradient(180deg,#3a2f45,#c27a3c)}
.t3{background:linear-gradient(160deg,#5a6673,#2a2a2a)}
.t4{background:linear-gradient(180deg,#0f3a4a,#1f6670)}
.t5{background:linear-gradient(160deg,#6b5d4a,#2f2a23)}
.t6{background:linear-gradient(160deg,#3a2a20,#7a5a3a)}
.t7{background:linear-gradient(180deg,#bcc8d6,#6f7f90)}
.t8{background:linear-gradient(160deg,#2f4a63,#8a6a5a)}
.t9{background:linear-gradient(160deg,#6a2e4a,#c98b45)}
.t10{background:linear-gradient(180deg,#314a66,#6d5a4a)}
.t11{background:linear-gradient(180deg,#8a7357,#3d4a3a)}
.t12{background:linear-gradient(160deg,#2c3a2a,#7a6a3a)}
.rule{height:1px;background:#dcdcdc;width:880px;margin:56px 0 0 -10px}

.ads{height:360px;padding-top:85px}
.ads .wrap{display:flex;justify-content:space-between}
.ad-stack{display:flex;flex-direction:column;gap:12px;margin-left:5px}
.ad{background:var(--ad);color:#fff;font-family:"Raleway",sans-serif;font-weight:700;font-size:20px;display:flex;align-items:center;justify-content:center}
.ad.wide{width:545px;height:60px}
.ad.box{width:242px;height:195px;margin-right:-20px;margin-top:-25px}

.blog{height:510px;padding-top:60px}
.posts{display:flex;gap:18px;margin:45px 0 0 5px}
.post{width:270px;background:#fff;box-shadow:0 1px 5px rgba(0,0,0,.15)}
.post .img{height:165px}
.p1{background:linear-gradient(180deg,#1c2a55,#b04a4a)}
.p2{background:linear-gradient(180deg,#a8c0d8,#7a6a5a)}
.p3{background:linear-gradient(180deg,#b7cde0,#c77c5f)}
.post-body{padding:12px 14px}
.post h4{text-align:center;font-size:14px;font-weight:700;color:#222}
.post p{font-size:10px;line-height:1.6;color:#777;margin-top:8px}
.meta{display:flex;justify-content:space-between;border-top:1px solid var(--line);margin-top:12px;padding-top:8px;font-size:9px;color:#888}
.view-more{display:block;width:195px;margin:26px auto 0;padding:8px 0;font-size:11px}

.footer{position:absolute;left:0;top:3700px;width:1200px;height:391px;background:var(--footer);color:#ccc}
.footer .wrap{display:flex;padding-top:65px}
.fcol h4{color:#fff;font-size:15px;font-weight:600;margin-bottom:12px}
.fcol p,.fcol li{font-size:11px;line-height:1.7}
.fcol ul{list-style:none}
.fcol li{display:flex;gap:6px;align-items:center}
.col-brand{width:235px;padding-right:20px}
.col-brand h4{font-size:22px;font-weight:500}
.col-contact{width:265px;padding-right:20px}
.col-contact li{margin-bottom:8px;align-items:flex-start}
.col-contact li svg{flex:0 0 auto;margin-top:4px}
.col-links{width:135px}
.col-news{width:225px}
.news-input{height:28px;background:#fff;margin-top:6px;font-size:10px;color:#999;padding:7px 8px}
.col-news .btn{margin-top:12px;padding:8px 22px}
.copy{position:absolute;bottom:0;width:100%;height:50px;background:var(--footer-deep);text-align:center;line-height:50px;font-size:10px;color:#bbb}
</style>
</head>
<body>

<header class="topbar">
  <div class="wrap">
    <span><svg width="9" height="9" viewBox="0 0 10 10"><path d="M2 1l2 2-1 1a6 6 0 003 3l1-1 2 2-1 2C4 10 0 6 0 2z" fill="#888"/></svg>0800 111 222</span>
    <span><svg width="10" height="8" viewBox="0 0 10 8"><rect x=".5" y=".5" width="9" height="7" fill="none" stroke="#888"/><path d="M.5 .5l4.5 4 4.5-4" fill="none" stroke="#888"/></svg>hello@vastelodge.net</span>
    <span>Login / Register</span>
    <span>Eng ▾</span>
  </div>
</header>

<nav class="nav">
  <div class="wrap">
    <div class="logo"><i></i>Vastelodge</div>
    <div class="menu">
      <a class="active">HOME</a><a>YOUR FAVORITES</a><a>BLOG</a><a>CONTACT US</a>
    </div>
  </div>
</nav>

<section class="hero" role="img" aria-label="Photo of friends sharing a meal outdoors on holiday">
  <h1 class="hero-title">ENJOY YOUR HOLIDAYS</h1>
  <div class="arrow left"><svg width="14" height="22" viewBox="0 0 14 22"><path d="M12 2L3 11l9 9" fill="none" stroke="#fff" stroke-width="3"/></svg></div>
  <div class="arrow right"><svg width="14" height="22" viewBox="0 0 14 22"><path d="M2 2l9 9-9 9" fill="none" stroke="#fff" stroke-width="3"/></svg></div>
  <form class="search">
    <div class="field"><label>ARRIVAL DATE</label><div class="input">12/08/2019</div></div>
    <div class="field"><label>DEPARTURE DATE</label><div class="input">19/08/2019</div></div>
    <div class="field"><label>GUESTS</label><div class="input">2 to 20 people</div></div>
    <span class="btn">Check Availability</span>
  </form>
</section>

<section class="welcome">
  <div class="wrap">
    <div class="welcome-text">
      <h2>Welcome To Vastelodge</h2>
      <span class="sub">High quality accommodation services</span>
      <p>Donec quis ante eget tellus varius suscipit. Duis a purus gravida, pretium lectus et, pretium enim. Maecenas tellus diam, lobortis eu scelerisque, placerat euismod arcu. Pellentesque, metus nec sodales consequat, neque libero semper tortor, at dapibus dolor quam sit at elit. Cras gravida diam sit amet fermentum accumsan, purus diam condimentum justo, vitae venenatis metus lorem sed elit. Suspendisse nisi nunc.</p>
      <span class="btn">REGISTER NOW</span>
    </div>
    <div class="welcome-photo" role="img" aria-label="Photo of a colourful old town street"></div>
  </div>
</section>

<section class="capacity" role="img" aria-label="Background photo of a tropical beach at dusk">
  <h2>Lodging By Capacity</h2>
  <div class="lead">Lorem ipsum dolor sit amet, consectetur adipiscing elit.</div>
  <div class="cap-row">
    <div class="cap"><div class="num">2-20</div><small>2 to 20 people</small></div>
    <div class="cap"><div class="num">20-40</div><small>20 to 40 People</small></div>
    <div class="cap"><div class="num">40-60</div><small>40 to 60 People</small></div>
    <div class="cap"><div class="num">60-80</div><small>60 to 80 People</small></div>
    <div class="cap"><div class="num">80-120</div><small>80 to 120 People</small></div>
    <div class="cap"><div class="num">120+</div><small>More Than 120 People</small></div>
  </div>
</section>

<section class="department">
  <h2 class="section-title">Lodging By Department</h2>
  <div class="wrap dept-body">
    <div class="dept-map"><div class="fill" role="img" aria-label="Map of French departments with Orne highlighted"></div></div>
    <div class="dept-info">
      <h3>ORNE</h3>
      <div class="kind">French Department</div>
      <p>Lorem Ipsum is simply dummy text of the printing and typesetting industry. Lorem Ipsum has been the industry's standard dummy text ever since the 1500s, when an unknown printer took a galley of type and scrambled it to make a type specimen book.</p>
      <div class="maps-label"><svg width="24" height="24" viewBox="0 0 24 24"><rect x="2" y="2" width="20" height="20" fill="#d9d9d9"/></svg>PlaneMaps</div>
    </div>
  </div>
</section>

<section class="themes">
  <h2 class="section-title">Lodging By Theme</h2>
  <div class="lead">Lorem ipsum dolor sit amet, consectetur adipiscing elit.</div>
  <div class="wrap">
    <div class="theme-grid">
      <div class="tile t1" role="img" aria-label="Seminar photo">Seminar</div>
      <div class="tile t2" role="img" aria-label="Beach sunset photo">Beach</div>
      <div class="tile t3" role="img" aria-label="Motorbike rider photo">Motorbike &amp; classic cars</div>
      <div class="tile t4" role="img" aria-label="Underwater photo">Aquatic</div>
      <div class="tile t5" role="img" aria-label="Horse photo">Horse riding</div>
      <div class="tile t6" role="img" aria-label="Dinner table photo">Gastronomic</div>
      <div class="tile t7" role="img" aria-label="Snowy landscape photo">Snow Nature and hike</div>
      <div class="tile t8" role="img" aria-label="Holiday photo">Lorem Ipsum</div>
      <div class="tile t9" role="img" aria-label="Festival crowd photo">Integration Weekend</div>
      <div class="tile t10" role="img" aria-label="Tents at a camp photo">Summer Camp</div>
      <div class="tile t11" role="img" aria-label="Mountain biking photo">Mountain Bike</div>
      <div class="tile t12" role="img" aria-label="Group of friends photo">Lorem Ipsum</div>
    </div>
    <div class="rule"></div>
  </div>
</section>

<section class="ads">
  <div class="wrap">
    <div class="ad-stack">
      <div class="ad wide">AD</div>
      <div class="ad wide">AD</div>
    </div>
    <div class="ad box">AD</div>
  </div>
</section>

<section class="blog">
  <h2 class="section-title">Blog</h2>
  <div class="wrap">
    <div class="posts">
      <article class="post">
        <div class="img p1" role="img" aria-label="Photo of a city tower at night"></div>
        <div class="post-body">
          <h4>Lorem Ipsum is simply</h4>
          <p>Lorem Ipsum is simply dummy text of the printing and typesetting industry. Lorem Ipsum has been the industry's standard dummy text ever [...]</p>
          <div class="meta"><span>● admin</span><span>April 02, 2019</span><span>0 Comments</span></div>
        </div>
      </article>
      <article class="post">
        <div class="img p2" role="img" aria-label="Photo of a bridge over a river"></div>
        <div class="post-body">
          <h4>Lorem Ipsum is simply</h4>
          <p>Lorem Ipsum is simply dummy text of the printing and typesetting industry. Lorem Ipsum has been the industry's standard dummy text ever [...]</p>
          <div class="meta"><span>● admin</span><span>April 02, 2019</span><span>0 Comments</span></div>
        </div>
      </article>
      <article class="post">
        <div class="img p3" role="img" aria-label="Photo of a colourful street"></div>
        <div class="post-body">
          <h4>Lorem Ipsum is simply</h4>
          <p>Lorem Ipsum is simply dummy text of the printing and typesetting industry. Lorem Ipsum has been the industry's standard dummy text ever [...]</p>
          <div class="meta"><span>● admin</span><span>April 02, 2019</span><span>0 Comments</span></div>
        </div>
      </article>
    </div>
    <span class="btn view-more">View More</span>
  </div>
</section>

<footer class="footer">
  <div class="wrap">
    <div class="fcol col-brand">
      <h4>Vastelodge</h4>
      <p>Lorem Ipsum is simply dummy text of the printing and typesetting industry. Lorem Ipsum has been the industry's standard dummy text ever since the 1500s, when an unknown.</p>
    </div>
    <div class="fcol col-contact">
      <h4>Contact Details</h4>
      <ul>
        <li><svg width="10" height="12" viewBox="0 0 10 12"><path d="M5 0a4 4 0 014 4c0 3-4 8-4 8S1 7 1 4a4 4 0 014-4z" fill="#c8115f"/></svg>Lorem Ipsum is simply dummy text of the printing and typesetting industry.</li>
        <li><svg width="10" height="8" viewBox="0 0 10 8"><rect width="10" height="8" fill="#c8115f"/></svg>hello@vastelodge.net</li>
        <li><svg width="10" height="10" viewBox="0 0 10 10"><path d="M2 1l2 2-1 1a6 6 0 003 3l1-1 2 2-1 2C4 10 0 6 0 2z" fill="#c8115f"/></svg>0800 111 222</li>
      </ul>
    </div>
    <div class="fcol col-links">
      <h4>Site Link</h4>
      <ul><li>› Home</li><li>› Your Favorites</li><li>› Blog</li><li>› FAQ</li><li>› Contact Us</li></ul>
    </div>
    <div class="fcol col-news">
      <h4>Signup For newsletter</h4>
      <div class="news-input">Email</div>
      <span class="btn">SIGN UP</span>
    </div>
  </div>
  <div class="copy">© copyright Vastelodge 2019 All rights reserved</div>
</footer>

</body>
</html>
```